Velmira - New coded website

Current website is around 5 years old and corrupted in some ways...
I would like to refresh the design and to create a new coded website based on the current content .
Please refer to :
www.velmira.com.au

Coding

Coded - Design and coding required

```html
<!DOCTYPE html>
<html lang="en">
<head>
<meta charset="utf-8">
<title>Velmira – Odours Controlled Naturally</title>
<link href="https://fonts.googleapis.com/css2?family=Poppins:wght@500;600;700&family=Inter:ital,wght@0,400;0,500;0,600;1,400&display=swap" rel="stylesheet">
<style>
:root{
  --green:#5cb531;
  --navy:#0b2434;
  --teal:#0d4e6c;
  --ink:#1c2a33;
  --muted:#55636b;
  --beige:#ede5d8;
  --field:#9fd17f;
  --footer:#0e2536;
  --footbar:#0d4c6b;
}
*{box-sizing:border-box;margin:0;padding:0}
html,body{width:1200px;height:2171px;overflow:hidden;background:#fff}
body{position:relative;font-family:"Inter",sans-serif;color:var(--ink)}
.abs{position:absolute}
.heading{font-family:"Poppins",sans-serif;font-weight:600;color:var(--teal)}
.btn{position:absolute;display:flex;align-items:center;justify-content:center;border-radius:22px;color:#fff;font-size:12px;font-weight:500;letter-spacing:.2px;background:var(--green)}
.btn.dark{background:var(--teal)}

/* header */
.brand{left:160px;top:24px;display:flex;align-items:center;gap:10px}
.brand-dot{width:52px;height:52px;border-radius:50%;background:var(--green)}
.brand-name{font-family:"Poppins",sans-serif;font-size:28px;font-weight:500;color:var(--teal)}
.top-contact{top:28px;font-size:12px;color:var(--ink);display:flex;align-items:center;gap:6px}
.nav{left:395px;top:69px;width:644px;display:flex;justify-content:space-between;font-size:11.5px;color:var(--ink);white-space:nowrap}

/* hero */
.hero-title{left:158px;top:170px;font-family:"Poppins",sans-serif;font-weight:700;color:var(--navy);line-height:1}
.hero-title .l1{font-size:77px;display:block}
.hero-title .l2{font-size:57px;display:block;margin-top:12px}
.hero-title .l3{font-size:57px;display:block;margin-top:6px;color:var(--green)}

/* features */
.card{position:absolute;top:614px;width:206px;height:56px;background:#fff;border-radius:6px;box-shadow:0 3px 14px rgba(0,0,0,.08);display:flex;align-items:center;gap:7px;padding:0 10px;font-size:11.6px;line-height:1.3;white-space:nowrap}
.card svg{flex:none}

/* about */
.video{left:159px;top:734px;width:430px;height:242px;border-radius:10px;background:linear-gradient(180deg,#d6ebc6 0%,#c5e3ae 60%,#8cc66a 100%)}
.play{left:350px;top:831px;width:48px;height:48px;border-radius:50%;background:#fff;box-shadow:0 2px 8px rgba(0,0,0,.15)}
.about-p{left:616px;top:813px;width:414px;font-size:11.6px;line-height:15px;color:var(--ink)}
.about-p em{font-style:normal;color:var(--green)}

/* testimonial */
.review{left:281px;top:1083px;width:647px;height:213px;background:#fff;border-radius:14px;box-shadow:0 4px 24px rgba(0,0,0,.08);padding:34px 37px}
.review .name{font-family:"Poppins",sans-serif;font-weight:600;font-size:14px;color:var(--green)}
.review .role{font-size:10px;margin-top:2px}
.review .lead{font-family:"Poppins",sans-serif;font-weight:500;font-size:14px;color:var(--teal);margin-top:8px}
.review .quote{font-style:italic;font-size:9.6px;line-height:15px;color:var(--muted);margin-top:12px}

/* clients */
.clients{left:0;top:1360px;width:1200px;height:121px;background:var(--beige)}
.arrow{position:absolute;width:38px;height:38px;border-radius:50%;background:var(--green);display:flex;align-items:center;justify-content:center}
.client{position:absolute;top:1404px;height:32px;display:flex;align-items:center;gap:6px;font-family:"Poppins",sans-serif;font-weight:600;font-size:16px;color:#3a3f44;white-space:nowrap}
.client i{display:block;width:22px;height:22px;border-radius:50%;background:#3a3f44}

/* contact */
.strip{left:0;top:1481px;width:66px;height:422px;background:var(--green)}
.field{position:absolute;border:1px solid var(--field);border-radius:5px;font-size:11px;color:#8a959b;padding:0 11px;display:flex;align-items:center}
.field.area{align-items:flex-start;padding-top:10px}
.map{left:684px;top:1481px;width:516px;height:422px;background:linear-gradient(135deg,#e2eef6,#cfe1ec)}

/* footer */
.footer{left:0;top:1903px;width:1200px;height:238px;background:var(--footer)}
.foot-h{position:absolute;top:1951px;font-family:"Poppins",sans-serif;font-weight:600;font-size:15px;color:#fff}
.foot-list{position:absolute;left:313px;top:1988px;list-style:none;font-size:10.5px;color:#fff;line-height:22.5px}
.foot-text{position:absolute;font-size:11.5px;color:#fff;line-height:16px}
.sub-box{left:760px;top:2045px;width:207px;height:35px;border-radius:18px;background:#fff;font-size:10px;color:#555;display:flex;align-items:center;padding-left:11px}
.sub-btn{left:893px;top:2045px;width:74px;height:35px;border-radius:18px;background:var(--green);color:#fff;font-size:10.5px;font-weight:500;display:flex;align-items:center;justify-content:center}
.footbar{left:0;top:2141px;width:1200px;height:30px;background:var(--footbar);font-size:10px;color:#fff}
</style>
</head>
<body>

<!-- header -->
<div class="abs brand"><span class="brand-dot"></span><span class="brand-name">Velmira</span></div>
<div class="abs top-contact" style="left:687px">
  <svg width="10" height="10" viewBox="0 0 24 24"><path fill="var(--teal)" d="M6.6 10.8a15 15 0 0 0 6.6 6.6l2.2-2.2c.3-.3.7-.4 1-.2 1.1.4 2.3.6 3.6.6.6 0 1 .4 1 1V20c0 .6-.4 1-1 1A17 17 0 0 1 3 4c0-.6.4-1 1-1h3.5c.6 0 1 .4 1 1 0 1.3.2 2.5.6 3.6.1.3 0 .7-.2 1z"/></svg>
  +61 (08) 5550 1200</div>
<div class="abs top-contact" style="left:829px">
  <svg width="12" height="9" viewBox="0 0 24 18"><rect width="24" height="18" rx="2" fill="var(--teal)"/><path d="M1 2l11 8 11-8" stroke="#fff" stroke-width="2" fill="none"/></svg>
  Email Us</div>
<div class="btn" style="left:904px;top:18px;width:135px;height:36px">REQUEST A QUOTE</div>
<nav class="abs nav">
  <span>Odour Control Products ▾</span><span>How Biofiltration Works ▾</span><span>Odour Control by Industry ▾</span><span>Past Projects</span><span>About Us</span><span>Contact</span>
</nav>

<!-- hero -->
<h1 class="abs hero-title"><span class="l1">Odours</span><span class="l2">Controlled</span><span class="l3">Naturally</span></h1>
<div class="btn" style="left:160px;top:398px;width:134px;height:36px">REQUEST A QUOTE</div>
<svg class="abs" style="left:540px;top:112px" width="400" height="400" viewBox="0 0 400 400">
  <defs><linearGradient id="photo" x1="0" y1="0" x2="0" y2="1"><stop offset="0" stop-color="#b8c9a2"/><stop offset=".5" stop-color="#9fb57e"/><stop offset="1" stop-color="#7d9a5a"/></linearGradient></defs>
  <path d="M 198 2 A 196 196 0 1 1 130 385" stroke="var(--green)" stroke-width="18" fill="none"/>
  <path d="M 120 380 A 196 196 0 0 1 28 120" stroke="var(--green)" stroke-width="18" fill="none"/>
  <path d="M 340 330 A 196 196 0 0 1 220 393" stroke="var(--teal)" stroke-width="18" fill="none"/>
  <circle cx="198" cy="198" r="178" fill="url(#photo)" role="img" aria-label="Photo of a woman outdoors with arms spread wide, breathing fresh air"/>
</svg>

<!-- features -->
<h2 class="abs heading" style="left:0;width:1200px;top:560px;text-align:center;font-size:26px">What makes us the best?</h2>
<div class="card" style="left:160px"><svg width="30" height="30" viewBox="0 0 32 32" fill="none" stroke="var(--green)" stroke-width="1.5"><circle cx="16" cy="16" r="8"/><path d="M16 4v4M16 24v4M4 16h4M24 16h4"/></svg><span>Biological &amp; Sustainable<br>technology</span></div>
<div class="card" style="left:386px"><svg width="30" height="30" viewBox="0 0 32 32" fill="none" stroke="var(--green)" stroke-width="1.5"><circle cx="18" cy="10" r="6"/><path d="M3 24h8l6 3 11-6"/></svg>Efficient maintenance cost</div>
<div class="card" style="left:609px"><svg width="34" height="30" viewBox="0 0 36 32" fill="none" stroke="var(--green)" stroke-width="1.5"><path d="M4 12l8-6 6 3 4-5 8 8-2 10-10 2-8-3-6 1z"/></svg>100% Australian Owned</div>
<div class="card" style="left:834px"><svg width="32" height="30" viewBox="0 0 34 32" fill="none" stroke="var(--green)" stroke-width="1.5"><circle cx="17" cy="16" r="13"/><path d="M11 20c0-7 5-10 12-10 0 7-4 11-12 10zM11 20l6-5"/></svg>Eco Friendly</div>

<!-- about -->
<div class="abs video" role="img" aria-label="Illustration of biofilter tanks among green hills and trees, with eco icons above"></div>
<div class="abs play"><svg width="48" height="48" viewBox="0 0 48 48"><path d="M19 15l14 9-14 9z" fill="var(--green)"/></svg></div>
<div class="abs" style="left:616px;top:746px;font-size:14px">Odour Control Solutions</div>
<h2 class="abs heading" style="left:616px;top:764px;font-size:26px">About Velmira</h2>
<p class="abs about-p">Velmira uses sustainable biotechnology to resolve odour and <em>corrosion</em> problems in a highly efficient, environmentally friendly and cost-effective manner. Our, products, the VelVent series of biofilters have been specifically engineered to overcome issues traditionally associated with biofiltration, such as bed compaction and uneven moisture levels, and our patented design achieves a removal rate of up to 99.9% per stage of treatment.</p>
<div class="btn" style="left:616px;top:925px;width:135px;height:36px">REQUEST A QUOTE</div>
<div class="btn dark" style="left:764px;top:925px;width:100px;height:36px">READ MORE</div>

<!-- testimonial -->
<h2 class="abs heading" style="left:0;width:1200px;top:1029px;text-align:center;font-size:26px">What people think about us</h2>
<div class="abs review">
  <div class="name">Tom Ellery</div>
  <div class="role">Nearby resident to Willow Street Pump Station</div>
  <div class="lead">As soon as the system was started, the smell disappeared!</div>
  <p class="quote">“Karl and the Velmira team promised to stop the odour from our smelly neighbor and they delivered- in spades! As soon as the system was started, the smell disappeared. The system is well designed, very professionally installed and the beauty of it is, apart from a constantly running fan, it is bacteria doing the heavy lifting, so it is very environmentally friendly. We lived with the smell for 3 three years which could be extremely frustrating and unpleasant. Now, the problem is solved and we can have BBQs again. We are happy and our neighbours have noticed the odour is gone. Thank you!”</p>
</div>

<!-- clients -->
<div class="abs clients"></div>
<h2 class="abs heading" style="left:160px;top:1382px;font-size:25px;line-height:36px">Our happy<br>clients</h2>
<div class="arrow" style="left:387px;top:1401px"><svg width="12" height="12" viewBox="0 0 12 12"><path d="M8 1L3 6l5 5" stroke="#fff" stroke-width="1.8" fill="none"/></svg></div>
<div class="client" style="left:458px"><i></i>Harbour City</div>
<div class="client" style="left:665px"><i></i>AquaState</div>
<div class="client" style="left:833px"><i></i>Ridge Territory</div>
<div class="arrow" style="left:987px;top:1401px"><svg width="12" height="12" viewBox="0 0 12 12"><path d="M4 1l5 5-5 5" stroke="#fff" stroke-width="1.8" fill="none"/></svg></div>

<!-- contact -->
<div class="abs strip"></div>
<h2 class="abs heading" style="left:160px;top:1536px;font-size:25px">Get in Contact</h2>
<p class="abs" style="left:160px;top:1584px;width:400px;font-size:11.5px;line-height:15px">If you have any queries regarding out products, please do not hesitate to contact us</p>
<div class="field" style="left:160px;top:1629px;width:206px;height:35px">First Name</div>
<div class="field" style="left:386px;top:1629px;width:206px;height:35px">Surname</div>
<div class="field" style="left:160px;top:1673px;width:206px;height:35px">Email</div>
<div class="field" style="left:386px;top:1673px;width:206px;height:35px">Phone</div>
<div class="field area" style="left:160px;top:1717px;width:431px;height:74px">Message</div>
<div class="btn" style="left:160px;top:1805px;width:64px;height:36px">SEND</div>
<div class="abs map" role="img" aria-label="Street map of the industrial area around the office with a location pin"></div>

<!-- footer -->
<div class="abs footer"></div>
<div class="abs" style="left:164px;top:1985px;display:flex;align-items:center;gap:10px"><span style="width:40px;height:40px;border-radius:50%;background:var(--green)"></span><span style="font-family:Poppins,sans-serif;font-size:26px;font-weight:500;color:#fff">Velmira</span></div>
<div class="foot-h" style="left:313px">Quick Menu</div>
<ul class="foot-list"><li>› ODOUR CONTROL PRODUCTS</li><li>HOW BIOFILTRATION WORKS</li><li>ODOUR CONTROL BY INDUSTRY</li><li>PAST PROJECTS</li><li>ABOUT US</li></ul>
<div class="foot-h" style="left:534px">Address</div>
<div class="foot-text" style="left:534px;top:1988px">☏&nbsp; +61 (08) 5550 1200</div>
<div class="foot-text" style="left:534px;top:2007px;width:200px">⌖&nbsp; 14 Marrow Lane, Brookvale WA 6099, Australia</div>
<div class="foot-text" style="left:534px;top:2048px">Connect Us: <b style="color:var(--green)">in</b></div>
<div class="foot-h" style="left:760px">Subscription</div>
<div class="foot-text" style="left:760px;top:1985px;font-weight:600;font-size:11.5px">Subscribe Us Now</div>
<div class="foot-text" style="left:760px;top:2005px;width:180px;font-size:8.5px;line-height:11px">Lorem ipsum dolor sit amet, consectetur adipiscing elit, sed do eiusmod tempor</div>
<div class="abs sub-box">Enter Your Email</div>
<div class="abs sub-btn">Subscribe</div>
<div class="abs" style="left:982px;top:1943px;width:50px;height:50px;border-radius:50%;background:var(--green)"></div>
<div class="abs" style="left:960px;top:2050px;width:95px;transform:rotate(90deg);font-family:Poppins,sans-serif;font-size:22px;font-weight:500;color:#fff;text-align:center">Velmira</div>
<div class="abs footbar">
  <span class="abs" style="left:160px;top:8px">Website by Pixelmoor</span>
  <span class="abs" style="right:169px;top:8px">Privacy Policy &nbsp;|&nbsp; Sitemap &nbsp;|&nbsp; ABN: 12 345 678 901</span>
</div>

</body>
</html>
```